Business cards and stationary for IT Service Provider
Quillon Datacraft
Business cards and stationary for IT Service Provider - Information Technology
Creative Brief
Use specific fonts
No preference, we have used is called ETHNOCENTRIC for the tagline
Bright & Fun-filled
Peter Hollins
Director
Meadowbank Upper Fenwick Lane Brindlow, Preston PR5 7QT
pete@orlendatacraft-mail.com
www.orlendatacraft-mail.com
VAT Number and company registration number to be included somewhere on business card. VAT Number: 846 227 51 Company Registration Number: 4918264 In addition to letterhead we would also like a continuation sheet.
All the information we require is listed above, everything else is entirely up to you!
quillondatacraft quillondatacraft
Please note that this project is for Business Cards AND Stationary. Could we see some Letterheads too?

```html
<!DOCTYPE html>
<html lang="en">
<head>
<meta charset="utf-8">
<title>Quillon Datacraft — Business Cards</title>
<link rel="stylesheet" href="https://fonts.googleapis.com/css2?family=Open+Sans:wght@400;600;700&display=swap">
<style>
  :root {
    --bg: #2a2a2c;
    --card: #f7f7f7;
    --teal: #2fb3a8;
    --grey: #5a5a5c;
    --ink: #3d3d3f;
    --muted: #777779;
    --rule: #cfcfd1;
    --white: #ffffff;
  }
  html, body {
    margin: 0;
    width: 1200px;
    height: 802px;
    overflow: hidden;
    background: var(--bg);
    font-family: "Open Sans", Arial, sans-serif;
  }
  .stage { position: relative; width: 1200px; height: 802px; }
  .card {
    position: absolute;
    width: 540px;
    height: 309px;
    background: var(--card);
    box-shadow: 0 10px 30px rgba(0,0,0,.45);
    overflow: hidden;
  }
  .card--front { left: 330px; top: 64px; }
  .card--back  { left: 330px; top: 428px; }
  .swoosh { position: absolute; left: 0; top: 0; width: 540px; height: 309px; }
  .brand {
    display: flex; align-items: center; gap: 8px;
    color: var(--teal); font-weight: 700; letter-spacing: .5px; white-space: nowrap;
  }
  .brand__mark { width: 12px; height: 12px; background: var(--teal); flex: none; }
  .card--front .brand { position: absolute; left: 30px; top: 28px; font-size: 24px; }
  .contact-list {
    position: absolute; left: 30px; top: 82px;
    margin: 0; padding: 0; list-style: none;
    font-size: 10.5px; color: var(--muted);
  }
  .contact-list li { display: flex; align-items: center; gap: 8px; height: 19px; white-space: nowrap; }
  .contact-list svg { width: 10px; height: 10px; fill: var(--grey); flex: none; }
  .person { position: absolute; right: 30px; top: 108px; text-align: right; }
  .person__name { margin: 0; font-size: 13px; font-weight: 600; color: var(--ink); letter-spacing: 1px; text-transform: uppercase; }
  .person__role { margin: 2px 0 0; font-size: 10px; color: var(--muted); }
  .divider { position: absolute; left: 250px; right: 30px; top: 148px; height: 1px; background: var(--rule); }
  .address { position: absolute; right: 30px; top: 168px; width: 220px; text-align: right; font-size: 10px; line-height: 1.5; color: var(--muted); margin: 0; font-style: normal; }
  .web {
    position: absolute; left: 30px; bottom: 12px;
    font-size: 11px; color: var(--white); letter-spacing: .3px;
  }
  .card--back .brand {
    position: absolute; left: 0; right: 0; top: 110px;
    justify-content: center; font-size: 34px;
  }
</style>
</head>
<body>
<main class="stage">

  <section class="card card--front" aria-label="Business card front">
    <svg class="swoosh" viewBox="0 0 540 309" aria-hidden="true">
      <path d="M0 236 C160 218 360 222 540 256 L540 268 C350 238 150 234 0 250 Z" fill="var(--grey)"/>
      <path d="M0 250 C150 234 350 238 540 268 L540 309 L0 309 Z" fill="var(--teal)"/>
    </svg>
    <div class="brand"><span class="brand__mark"></span>Quillon Datacraft</div>
    <ul class="contact-list">
      <li><svg viewBox="0 0 10 10"><path d="M2 0h2l1 3-1.5 1a6 6 0 0 0 2.5 2.5L7 5l3 1v2a2 2 0 0 1-2 2A8 8 0 0 1 0 2a2 2 0 0 1 2-2z"/></svg>020 555 0147</li>
      <li><svg viewBox="0 0 10 10"><rect x="2" y="0" width="6" height="10" rx="1"/></svg>020 555 0148</li>
      <li><svg viewBox="0 0 10 10"><rect x="0" y="3" width="10" height="5"/><rect x="2" y="0" width="6" height="3"/></svg>020 555 0149</li>
      <li><svg viewBox="0 0 10 10"><path d="M0 2h10v6H0z"/></svg>pete@quillondatacraft-mail.com</li>
      <li><svg viewBox="0 0 10 10"><circle cx="5" cy="5" r="5"/></svg>www.quillondatacraft-mail.com</li>
      <li><svg viewBox="0 0 10 10"><rect x="0" y="0" width="10" height="10" rx="2"/></svg>VAT 846 227 51 · Reg 4918264</li>
    </ul>
    <div class="person">
      <p class="person__name">Peter Hollins</p>
      <p class="person__role">Director</p>
    </div>
    <div class="divider"></div>
    <address class="address">Meadowbank Upper Fenwick Lane<br>Brindlow, Preston PR5 7QT</address>
    <div class="web">www.quillondatacraft-mail.com</div>
  </section>

  <section class="card card--back" aria-label="Business card back">
    <svg class="swoosh" viewBox="0 0 540 309" aria-hidden="true">
      <path d="M0 236 C160 218 360 222 540 256 L540 268 C350 238 150 234 0 250 Z" fill="var(--grey)"/>
      <path d="M0 250 C150 234 350 238 540 268 L540 309 L0 309 Z" fill="var(--teal)"/>
    </svg>
    <div class="brand"><span class="brand__mark"></span>Quillon Datacraft</div>
    <div class="web">www.quillondatacraft-mail.com</div>
  </section>

</main>
</body>
</html>
```